Business Card Design

We need a design for business cards for our company. We have a logo. We teach EMT's and we are based out of Virginia. The information that will need to add would be, name, title, phone number, email, address. On the back of the business card would be "We help you, help others"

Target Market(s)

People that want to become EMT's

Colors

Designer to choose colors to be used in the design.

Requirements
Must have
• company logo

```html
<!DOCTYPE html>
<html lang="en">
<head>
<meta charset="utf-8">
<title>Crest Rescue Training – Business Card</title>
<link href="https://fonts.googleapis.com/css2?family=Lato:wght@400;700&family=Raleway:wght@600;700&display=swap" rel="stylesheet">
<style>
  :root {
    --bg: #e9e7e5;
    --card-front: #fbfbfa;
    --card-back: #1e2a33;
    --brand-red: #d21e3a;
    --ink: #2b2b2b;
    --grey: #8a8f94;
    --rule: #d6d6d6;
    --back-grey: #b9bec3;
  }
  * { margin: 0; padding: 0; box-sizing: border-box; }
  html, body { width: 1200px; height: 844px; overflow: hidden; }
  body {
    background: var(--bg);
    font-family: "Lato", Arial, sans-serif;
    position: relative;
  }
  .card {
    position: absolute;
    top: 279px;
    width: 500px;
    height: 286px;
    border-radius: 3px;
    box-shadow: 0 6px 18px rgba(0,0,0,.18);
  }
  .card--front { left: 60px; background: var(--card-front); }
  .card--back  { left: 640px; background: var(--card-back); }

  .brand {
    position: absolute;
    display: flex;
    align-items: center;
    gap: 8px;
    font-family: "Raleway", Arial, sans-serif;
    font-weight: 700;
    font-size: 21px;
    letter-spacing: .5px;
    color: var(--brand-red);
    text-transform: uppercase;
    white-space: nowrap;
  }
  .brand__dot {
    width: 12px; height: 12px;
    border-radius: 50%;
    background: var(--brand-red);
  }
  .card--front .brand { left: 200px; top: 44px; }
  .card--back .brand { left: 50%; top: 104px; transform: translateX(-50%); }

  .rule {
    position: absolute;
    right: 0;
    height: 1px;
    background: var(--rule);
  }
  .rule--top { top: 120px; left: 260px; }
  .rule--bottom { top: 142px; left: 200px; }

  .contact {
    position: absolute;
    left: 26px;
    bottom: 22px;
    color: var(--ink);
  }
  .contact__name {
    font-family: "Raleway", Arial, sans-serif;
    font-weight: 700;
    font-size: 17px;
    color: var(--brand-red);
    text-transform: uppercase;
    line-height: 1;
  }
  .contact__title { font-size: 13px; margin-top: 2px; }
  .contact__line { font-size: 13px; margin-top: 10px; }
  .contact__label { color: var(--brand-red); font-weight: 700; }

  .tagline {
    position: absolute;
    left: 0; right: 0;
    top: 182px;
    text-align: center;
    font-family: "Raleway", Arial, sans-serif;
    font-weight: 600;
    font-size: 13px;
    letter-spacing: .3px;
    text-transform: uppercase;
  }
  .tagline__lead { color: var(--brand-red); }
  .tagline__rest { color: var(--back-grey); }
</style>
</head>
<body>
  <section class="card card--front" aria-label="Business card front">
    <div class="brand"><span class="brand__dot"></span>Crest Rescue Training</div>
    <div class="rule rule--top"></div>
    <div class="rule rule--bottom"></div>
    <div class="contact">
      <p class="contact__name">Daniel Harper</p>
      <p class="contact__title">Managing Director</p>
      <p class="contact__line">18 Harbor Lane, Richmond VA, 23219</p>
      <p class="contact__line"><span class="contact__label">P:</span> 044-555 012 345 | <span class="contact__label">E:</span> hello@crestrescue.com</p>
    </div>
  </section>

  <section class="card card--back" aria-label="Business card back">
    <div class="brand"><span class="brand__dot"></span>Crest Rescue Training</div>
    <p class="tagline"><span class="tagline__lead">We help you,</span> <span class="tagline__rest">help others</span></p>
  </section>
</body>
</html>
```